Norvane. business card

We need a business card design for a new mobile car-wash catered toward urban residents. The use of colour should be black, white and red and should be sleek and minimal. The final design should be modern and enticing to look at. A picture of the logo is attached. The font and design should resemble something similar to the logo.

```html
<!DOCTYPE html>
<html lang="en">
<head>
<meta charset="utf-8">
<title>Norvane. business card</title>
<link rel="stylesheet" href="https://fonts.googleapis.com/css2?family=Questrial&family=Didact+Gothic&display=swap">
<style>
  :root {
    --stage: #d9d9d9;
    --black: #0b0b0b;
    --white: #ffffff;
    --red: #d4141b;
    --red-dark: #7a0a0e;
    --grey: #6b6b6b;
    --ink: #2a2a2a;
  }
  * { margin: 0; padding: 0; box-sizing: border-box; }
  html, body { width: 1200px; height: 871px; overflow: hidden; }
  body {
    background: var(--stage);
    position: relative;
    font-family: "Didact Gothic", "Questrial", sans-serif;
  }
  .card {
    position: absolute;
    width: 600px;
    height: 343px;
    overflow: hidden;
    box-shadow: 0 14px 30px rgba(0,0,0,.35);
  }
  /* Back side */
  .card--back { left: 90px; top: 80px; background: var(--black); }
  .card--back .brand {
    position: absolute; left: 70px; top: 138px;
    display: flex; align-items: center; gap: 10px;
  }
  .brand__mark { width: 14px; height: 14px; background: var(--red); }
  .brand__name {
    font-family: "Questrial", sans-serif;
    font-size: 40px; letter-spacing: 4px;
  }
  .card--back .brand__name { color: var(--white); }
  .card--back .web {
    position: absolute; left: 96px; top: 200px;
    color: var(--red); font-size: 14px; letter-spacing: 1px;
  }
  .skyline-area {
    position: absolute; right: 0; bottom: 0;
    width: 280px; height: 250px;
    background: linear-gradient(180deg, var(--red) 0%, var(--red-dark) 100%);
  }
  /* Front side */
  .card--front { left: 520px; top: 450px; background: linear-gradient(135deg, #ffffff 40%, #efefef 100%); }
  .card--front .brand {
    position: absolute; left: 48px; top: 120px;
    display: flex; align-items: center; gap: 10px;
  }
  .card--front .brand__name { color: var(--grey); }
  .person { position: absolute; left: 340px; top: 90px; }
  .person__name { color: var(--red); font-size: 20px; font-weight: bold; font-family: "Questrial", sans-serif; }
  .person__role { color: var(--grey); font-size: 14px; margin-top: 4px; }
  .contacts { position: absolute; left: 340px; top: 170px; list-style: none; }
  .contacts li {
    display: flex; align-items: center; gap: 14px;
    color: var(--ink); font-size: 15px; height: 22px;
  }
  .contacts svg { width: 12px; height: 12px; fill: var(--red); flex: none; }
  .edge-band { position: absolute; left: 0; right: 0; bottom: 18px; height: 16px; display: flex; gap: 6px; }
  .edge-band__red { width: 60px; background: var(--red); }
  .edge-band__black { flex: 1; background: linear-gradient(90deg, var(--black) 40%, rgba(11,11,11,0) 100%); }
</style>
</head>
<body>
  <section class="card card--back">
    <div class="brand">
      <span class="brand__mark"></span>
      <span class="brand__name">Norvane.</span>
    </div>
    <p class="web">www.norvane.com</p>
    <div class="skyline-area" role="img" aria-label="Red city skyline decoration"></div>
  </section>

  <section class="card card--front">
    <div class="brand">
      <span class="brand__mark"></span>
      <span class="brand__name">Norvane.</span>
    </div>
    <div class="person">
      <p class="person__name">Marek T Olsen</p>
      <p class="person__role">Ceo</p>
    </div>
    <ul class="contacts">
      <li><svg viewBox="0 0 12 12"><path d="M1 4c0-2 2-3 5-3s5 1 5 3l-2 1-1-2H4L3 5zM3 6h6l1 5H2z"/></svg>31 406 2291</li>
      <li><svg viewBox="0 0 12 12"><path d="M2 3h8v8H2zM4 0h4v3H4z"/></svg>74 219 6630</li>
      <li><svg viewBox="0 0 12 12"><path d="M3 0h6v12H3zM4 1v8h4V1z"/></svg>31 406 2295</li>
      <li><svg viewBox="0 0 12 12"><path d="M0 2h12v8H0zM1 3l5 4 5-4v-.5L6 6 1 2.5z"/></svg>marekolsen@mailbox.com</li>
    </ul>
    <div class="edge-band">
      <span class="edge-band__red"></span>
      <span class="edge-band__black"></span>
    </div>
  </section>
</body>
</html>
```